Creative - Appealing - Business Card Design Project

Looking for a Business card design (vector artwork) for an existing company called 'Copperfield Sound'. We operate in the entertainment industry specializing in audio system design and rental, however; we also deal with other sectors of the entertainment industry including lighting, video, staging and power system design and rental. We would like to see designs that don't focus too much on audio but include elements encompassing everything else.

Double sided business card, following our new colour scheme and logo, which is attached. The card would ideally be creative and eye catching to draw in new customers in the elegant event production market, such as weddings & corporate affairs.

Target Market(s)

High end corporate clients, wedding clients

Industry/Entity Type

Entertainment

Requirements
Must have
• Our contact details, these can be worded & listed however you think appropriate as part as the design

Business Name - Copperfield Sound
My Name - Benedict Thornbury
Web Address - www.copperfieldsound-example.com
Mobile Number - 07914 362 517
Office Number - 0330 411 7785
Email - ben@copperfieldsound-example.com

The name, email and mobile number would need to be able to be changed to my business partners also.

The font used on our logo is Sansation
Nice to have
• On one side maybe a word cloud involving the services in which we can provide; Lighting, Sound, Event Production, Staging, LED Uplighting, Projection Mapping, Wedding Hire

On the other side, all the important credentials of contact.
Should not have
• The design should not use any old style fonts (i.e Times New Roman, Gothic etc) or on the other side of the scale, any 'jokey' fonts (i.e. Comic Sans).

The font to be used is Sansation

```html
<!DOCTYPE html>
<html lang="en">
<head>
<meta charset="utf-8">
<title>Copperfield Sound – Business Card</title>
<link rel="stylesheet" href="https://fonts.googleapis.com/css2?family=Sansation:wght@400;700&display=swap">
<style>
  :root {
    --backdrop: #222222;
    --purple: #3a1d62;
    --purple-deep: #1b0a30;
    --purple-glow: #5b3b92;
    --silver-light: #f7f7f7;
    --silver-mid: #c9c9c9;
    --silver-dark: #8e8e8e;
    --brand-grey: #8a8a8a;
    --brand-purple: #4b2b86;
    --text-light: #ffffff;
  }
  html, body {
    margin: 0;
    width: 1200px;
    height: 1200px;
    overflow: hidden;
    background: var(--backdrop);
  }
  .sheet {
    position: relative;
    width: 1200px;
    height: 1200px;
  }
  .card {
    position: absolute;
    top: 441px;
    width: 556px;
    height: 318px;
    display: block;
  }
  .card--front { left: 33px; }
  .card--back { left: 611px; }
  .card text {
    font-family: "Sansation", "Trebuchet MS", sans-serif;
    fill: var(--text-light);
  }
  .holder-name { font-size: 24px; font-weight: 700; }
  .contact-line { font-size: 19px; font-weight: 400; }
  .service-item { font-size: 19px; font-weight: 700; }
  .card text.brand-name { font-size: 27px; font-weight: 700; fill: var(--brand-grey); }
  .card text.brand-name--back { font-size: 23px; fill: #707070; }
  .icon { fill: none; stroke: #e8e8e8; stroke-width: 1.4; }
  .icon-fill { fill: #e8e8e8; }
  .bullet { fill: none; stroke: #e8e8e8; stroke-width: 2; }
</style>
</head>
<body>
<main class="sheet">

  <!-- Front: contact details -->
  <svg class="card card--front" viewBox="0 0 593 339" xmlns="http://www.w3.org/2000/svg" aria-label="Business card front with contact details">
    <defs>
      <radialGradient id="frontPurple" cx="0.55" cy="0.4" r="0.8">
        <stop offset="0" stop-color="var(--purple)"/>
        <stop offset="1" stop-color="var(--purple-deep)"/>
      </radialGradient>
      <linearGradient id="frontChrome" x1="0" y1="0" x2="1" y2="1">
        <stop offset="0" stop-color="var(--silver-dark)"/>
        <stop offset="0.35" stop-color="var(--silver-light)"/>
        <stop offset="0.55" stop-color="var(--silver-dark)"/>
        <stop offset="0.75" stop-color="var(--silver-light)"/>
        <stop offset="1" stop-color="var(--silver-mid)"/>
      </linearGradient>
      <radialGradient id="frontPanel" cx="0.3" cy="0.2" r="0.9">
        <stop offset="0" stop-color="#ffffff"/>
        <stop offset="0.6" stop-color="#e3e3e3"/>
        <stop offset="1" stop-color="#b8b8b8"/>
      </radialGradient>
    </defs>
    <rect class="card-base" width="593" height="339" fill="url(#frontPurple)"/>
    <polygon class="card-shadow" points="0,0 262,0 462,212 0,258" fill="var(--purple-deep)" opacity="0.6"/>
    <polygon class="chrome-band" points="0,0 252,0 452,205 0,250" fill="url(#frontChrome)"/>
    <polygon class="silver-panel" points="0,0 240,0 358,163 0,229" fill="url(#frontPanel)" stroke="#9a9a9a" stroke-width="1"/>

    <circle class="brand-dot" cx="60" cy="98" r="26" fill="var(--brand-purple)"/>
    <text class="brand-name" x="26" y="170">Copperfield Sound</text>

    <text class="holder-name" x="567" y="47" text-anchor="end">Benedict Thornbury</text>

    <text class="contact-line" x="541" y="228" text-anchor="end">07914 362 517</text>
    <g class="icon-mobile" transform="translate(551,210)">
      <rect class="icon" x="0" y="0" width="10" height="18" rx="1.5"/>
      <rect class="icon-fill" x="2.5" y="3" width="5" height="6"/>
    </g>

    <text class="contact-line" x="541" y="258" text-anchor="end">0330 411 7785</text>
    <g class="icon-phone" transform="translate(548,243)">
      <path class="icon-fill" d="M1 5 Q9 -1 17 5 L15 8 L12 6 L6 6 L3 8 Z"/>
      <rect class="icon-fill" x="4" y="8" width="10" height="7" rx="1"/>
    </g>

    <text class="contact-line" x="541" y="288" text-anchor="end">ben@copperfieldsound-example.com</text>
    <g class="icon-mail" transform="translate(548,275)">
      <rect class="icon-fill" x="0" y="3" width="17" height="12" rx="1"/>
      <path d="M0 4 L8.5 10 L17 4" fill="none" stroke="#3a1d62" stroke-width="1.4"/>
    </g>

    <text class="contact-line" x="26" y="320">www.copperfieldsound-example.com</text>
  </svg>

  <!-- Back: services -->
  <svg class="card card--back" viewBox="0 0 593 339" xmlns="http://www.w3.org/2000/svg" aria-label="Business card back listing services">
    <defs>
      <linearGradient id="backChrome" x1="0" y1="0" x2="1" y2="1">
        <stop offset="0" stop-color="var(--silver-mid)"/>
        <stop offset="0.3" stop-color="var(--silver-light)"/>
        <stop offset="0.5" stop-color="var(--silver-dark)"/>
        <stop offset="0.7" stop-color="var(--silver-light)"/>
        <stop offset="1" stop-color="var(--silver-mid)"/>
      </linearGradient>
      <linearGradient id="backBand" x1="0" y1="1" x2="1" y2="0">
        <stop offset="0" stop-color="var(--purple-deep)"/>
        <stop offset="0.7" stop-color="var(--purple-glow)"/>
        <stop offset="1" stop-color="var(--purple)"/>
      </linearGradient>
      <radialGradient id="backPurple" cx="0.35" cy="0.35" r="0.7">
        <stop offset="0" stop-color="var(--purple-glow)"/>
        <stop offset="1" stop-color="var(--purple-deep)"/>
      </radialGradient>
    </defs>
    <rect class="card-base" width="593" height="339" fill="url(#backChrome)"/>
    <polygon class="outer-band" points="0,0 322,0 588,275 0,328" fill="url(#backBand)"/>
    <polygon class="inner-chrome" points="0,0 302,0 472,216 0,302" fill="url(#backChrome)"/>
    <polygon class="inner-panel" points="0,0 295,0 460,212 0,296" fill="url(#backPurple)"/>

    <text class="brand-name brand-name--back" x="567" y="50" text-anchor="end">Copperfield Sound</text>

    <g class="service-list">
      <circle class="bullet" cx="26" cy="36" r="7"/>
      <text class="service-item" x="50" y="42">Lighting</text>
      <circle class="bullet" cx="26" cy="69" r="7"/>
      <text class="service-item" x="50" y="75">Sound</text>
      <circle class="bullet" cx="26" cy="102" r="7"/>
      <text class="service-item" x="50" y="108">Event Production</text>
      <circle class="bullet" cx="26" cy="135" r="7"/>
      <text class="service-item" x="50" y="141">Staging</text>
      <circle class="bullet" cx="26" cy="168" r="7"/>
      <text class="service-item" x="50" y="174">LED Uplighting</text>
      <circle class="bullet" cx="26" cy="201" r="7"/>
      <text class="service-item" x="50" y="207">Projection Mapping</text>
      <circle class="bullet" cx="26" cy="234" r="7"/>
      <text class="service-item" x="50" y="240">Wedding Hire</text>
    </g>
  </svg>

</main>
</body>
</html>
```